Marcus Delwyn-Hart Finance

Need a personal website advertising Equipment Finance,Business Finance,Commercial Finance, Construction Finance, Bridging Finance. Similar websites are www.qorvimark.com.au / www.talsbrio.com.au / www.zpk7.com.au /wwwlemberwick.com.au

Target Market(s)

Business People

Industry/Entity Type

Business

Number of Pages Required

3 page

Font styles to use
Serif
Sans Serif

Requirements
Must have
• All i want is a simple corporate looking website advertising Equipment Finance, Commercial Finance, Construction Finance, Business Finance, Bridging Finance,

```html
<!DOCTYPE html>
<html lang="en">
<head>
<meta charset="utf-8">
<title>Marcus Finance</title>
<link href="https://fonts.googleapis.com/css2?family=Figtree:wght@400;500;600;700;800&display=swap" rel="stylesheet">
<style>
:root{
  --blue:#1e9ff2;
  --navy:#1f2e45;
  --text:#555d66;
  --muted:#8a9199;
  --line:#d9dde2;
  --band:#f2f2f2;
  --footer:#151c26;
  --white:#ffffff;
}
*{margin:0;padding:0;box-sizing:border-box}
html,body{width:1200px;height:2765px;overflow:hidden}
body{position:relative;font-family:"Figtree",Arial,sans-serif;color:var(--text);background:var(--white)}
.abs{position:absolute}
.accent{color:var(--blue)}

/* header */
.site-header{left:0;top:0;width:1200px;height:107px;background:var(--white);box-shadow:0 2px 6px rgba(0,0,0,.12);z-index:2}
.brand{left:79px;top:28px;display:flex;align-items:center;gap:14px;font-size:30px;font-weight:700;color:var(--navy)}
.brand-square{width:46px;height:46px;background:var(--blue)}
.main-nav{left:616px;top:44px;display:flex;gap:0;font-size:16px;font-weight:500;color:var(--navy)}
.main-nav span{display:inline-block}
.nav-home{width:127px;text-align:left;padding-left:0;text-decoration:underline;text-decoration-color:var(--muted)}
.nav-about{width:116px}
.phone-box{left:942px;top:40px;width:177px;height:36px;border:1px solid var(--line);display:flex;align-items:center;font-size:16px;color:var(--navy)}
.phone-icon{width:36px;height:36px;background:var(--blue);display:flex;align-items:center;justify-content:center;margin:-1px 16px 0 -1px}

/* hero */
.hero{left:0;top:107px;width:1200px;height:509px;background:linear-gradient(100deg,#3a4356 0%,#8b8f99 35%,#d8d6d1 60%,#e9e7e3 80%,#a9a7a3 100%)}
.hero-copy{right:234px;top:268px;text-align:right;color:var(--navy)}
.hero-title{font-size:38px;font-weight:700;line-height:1}
.hero-text{margin-top:14px;font-size:17px;line-height:24px;color:#4a5360}
.btn{display:inline-block;background:var(--blue);color:var(--white);font-weight:600;text-align:center}
.hero-btn{margin-top:16px;width:116px;height:30px;line-height:30px;font-size:14px}
.hero-arrows{right:234px;top:422px;display:flex;gap:4px}
.hero-arrows span{width:20px;height:20px;display:flex;align-items:center;justify-content:center;border:1px solid #999;background:#eee}
.hero-arrows span.on{background:var(--blue);border-color:var(--blue)}

/* about */
.section-title{font-size:33px;font-weight:700;color:var(--navy)}
.about-title{left:79px;top:670px}
.about-rule{left:79px;top:728px;width:680px;height:1px;background:var(--line)}
.about-lede{left:79px;top:744px;width:680px;font-size:15px;line-height:24px;font-weight:700;color:var(--navy)}
.about-body{left:79px;top:796px;width:680px;font-size:13.5px;line-height:26px;color:var(--text)}
.about-btn{left:79px;top:1021px;width:144px;height:39px;line-height:39px;font-size:15px}

.inquiry{left:791px;top:673px;width:328px;height:387px;border:1px solid var(--line);background:var(--white)}
.inquiry-head{height:70px;background:var(--blue);border-bottom:6px solid var(--navy);color:var(--white);font-size:29px;font-weight:700;text-align:center;line-height:64px}
.field{position:absolute;left:17px;width:293px;border:1px solid var(--line);background:#f5f6f7;font-size:13px;color:var(--navy);padding:10px 10px}
.field b{color:var(--blue);font-weight:400}
.f-name{top:95px;height:38px}
.f-email{top:144px;height:39px}
.f-service{top:194px;height:41px}
.f-service .caret{position:absolute;right:0;top:0;width:36px;height:39px;border-left:1px solid var(--line);display:flex;align-items:center;justify-content:center}
.f-address{top:244px;height:66px}
.submit{position:absolute;left:17px;top:321px;width:293px;height:39px;line-height:39px;font-size:16px}

/* services */
.services{left:0;top:1113px;width:1200px;height:737px;background:var(--band)}
.center-title{left:0;width:1200px;text-align:center}
.services-title{top:1168px}
.divider{left:494px;width:230px;height:14px}
.divider::before{content:"";position:absolute;left:0;right:0;top:7px;height:1px;background:#c8ccd1}
.divider span{position:absolute;left:108px;top:0;width:14px;height:14px;background:var(--navy);border:2px solid var(--band)}
.services-intro{left:100px;top:1248px;width:1000px;text-align:center;font-size:15px;line-height:29px;font-weight:600;color:var(--navy)}
.service-ring{left:0;top:0}
.svc-icon{width:83px;height:83px}
.svc-icon .frame{position:absolute;left:7px;top:-7px;width:83px;height:83px;border:3px solid var(--navy)}
.svc-icon .tile{position:absolute;left:0;top:0;width:83px;height:83px;background:var(--blue);border:4px solid var(--navy);display:flex;align-items:center;justify-content:center}
.core{left:544px;top:1557px;width:114px;height:118px}
.core .frame{position:absolute;inset:0;border:3px solid var(--navy)}
.core .tile{position:absolute;left:10px;top:10px;width:94px;height:98px;background:var(--blue)}
.svc-label{width:300px}
.svc-label h3{font-size:19px;font-weight:700;color:var(--navy);line-height:24px}
.svc-label p{margin-top:4px;font-size:13px;line-height:19px;color:var(--muted)}
.right-al{text-align:right}

/* blog */
.blog-title{top:1909px}
.blog-divider{top:1958px}
.blog-divider span{border-color:var(--white)}
.post{top:2016px;width:330px}
.post-photo{height:181px}
.post-date{position:absolute;left:0;top:0;width:57px;text-align:center;color:var(--white);font-weight:700}
.post-date .dm{background:var(--blue);height:59px;padding-top:9px;font-size:15px;line-height:20px}
.post-date .yr{background:var(--navy);height:46px;line-height:46px;font-size:14px}
.post h4{margin-top:26px;font-size:15px;font-weight:800;color:var(--navy)}
.post p{margin-top:12px;font-size:13px;line-height:19px;color:var(--text)}
.post-meta{margin-top:14px;border-top:1px solid var(--line);padding-top:10px;font-size:12px;color:var(--muted);display:flex}
.post-meta strong{color:var(--navy)}
.post-meta .sep{border-left:1px solid var(--line);margin:0 10px;height:16px}

/* footer */
.site-footer{left:0;top:2409px;width:1200px;height:309px;background:linear-gradient(90deg,#111821,#1d2632 50%,#111821)}
.foot-head{top:2454px;font-size:15px;font-weight:800;color:var(--white);text-transform:uppercase}
.foot-head::after{content:"";display:block;width:134px;height:1px;background:#3a4452;margin-top:10px}
.foot-links{left:79px;top:2500px;font-size:13px;line-height:34px;color:#cfd4da;list-style:none}
.foot-links li::before{content:"· ";color:var(--muted)}
.foot-links .current{color:var(--blue)}
.foot-square{left:79px;top:2603px;width:68px;height:68px;background:#4a5360}
.contact{left:315px;top:2500px;width:220px;color:#cfd4da;font-size:14px;line-height:20px}
.contact .name{color:var(--white);font-weight:700}
.contact .row{display:flex;align-items:center;gap:14px;color:var(--white);font-weight:600}
.map{left:617px;top:2505px;width:271px;height:200px;background:linear-gradient(135deg,#dcdad3,#c9c7bf);border:3px solid var(--white)}
.social{left:990px;top:2502px;list-style:none}
.social li{display:flex;align-items:center;gap:14px;height:46px;font-size:13px;font-weight:600;color:var(--white)}
.social .dot{width:34px;height:34px;border-radius:50%;background:var(--blue)}
.copyright{left:0;top:2718px;width:1200px;height:47px;background:var(--blue);color:var(--white);text-align:center;line-height:47px;font-size:13px;font-weight:600}
</style>
</head>
<body>

<header class="site-header abs">
  <div class="brand abs"><span class="brand-square"></span><span>Marcus Finance</span></div>
  <nav class="main-nav abs"><span class="nav-home">Home</span><span class="nav-about">About Us</span><span>Services</span></nav>
  <div class="phone-box abs">
    <span class="phone-icon"><svg width="16" height="16" viewBox="0 0 24 24"><path fill="#fff" d="M6.6 10.8a15 15 0 0 0 6.6 6.6l2.2-2.2c.3-.3.7-.4 1-.2 1.1.4 2.3.6 3.6.6.6 0 1 .4 1 1V20c0 .6-.4 1-1 1A17 17 0 0 1 3 4c0-.6.4-1 1-1h3.5c.6 0 1 .4 1 1 0 1.3.2 2.5.6 3.6.1.3 0 .7-.2 1z"/></svg></span>
    0198 765 432
  </div>
</header>

<section class="hero abs" role="img" aria-label="Photo of two businessmen in suits reviewing a document at an office desk"></section>
<div class="hero-copy abs">
  <h1 class="hero-title">Business Finance</h1>
  <p class="hero-text">Lorem ipsum dolor sit amet, consectetuer adipiscing elit,<br>sed diam nonummy nibhLorem ipsum dolor sit amet,</p>
  <span class="btn hero-btn">Call Us Today</span>
</div>
<div class="hero-arrows abs">
  <span><svg width="8" height="8" viewBox="0 0 8 8"><path d="M6 0v8L1 4z" fill="#333"/></svg></span>
  <span class="on"><svg width="8" height="8" viewBox="0 0 8 8"><path d="M2 0v8l5-4z" fill="#fff"/></svg></span>
</div>

<h2 class="section-title about-title abs">About Marcus <span class="accent">Finance</span></h2>
<div class="about-rule abs"></div>
<p class="about-lede abs">Lorem ipsum dolor sit amet, consectetuer adipiscing elit, sed diam nonummy nibh euismod tincidunt ut laoreet dolore magna aliquam erat volutpat.</p>
<p class="about-body abs">Lorem ipsum dolor sit amet, consectetuer adipiscing elit, sed diam nonummy nibh euismod tincidunt ut laoreet dolore magna aliquam erat volutpat. Ut wisi enim ad minim veniam, quis nostrud exerci tation ullamcorper suscipit lobortis nisl ut aliquip ex ea commodo consequat. Duis autem vel eum iriure dolor in hendrerit in vulputate velit esse molestie consequat, vel illum dolore eu feugiat nulla facilisis at vero eros et accumsan et iusto odio dignissim qui blandit praesent luptatum zzril delenit augue Duis dolore te feugait nulla facilisi. Lorem ipsum dolor sit amet, consectetuer adipiscing elit, sed diam nonummy nibh euismod tincidunt ut laoreet dolore magna aliquam erat volutpat. Ut wisi enim ad minim veniam, quis nostrud exerci tation ullamcorper</p>
<span class="btn about-btn abs">Read More</span>

<form class="inquiry abs">
  <div class="inquiry-head">Quick Inquiry</div>
  <div class="field f-name">Name <b>*</b></div>
  <div class="field f-email">Email <b>*</b></div>
  <div class="field f-service">Services <b>*</b><span class="caret"><svg width="12" height="7" viewBox="0 0 12 7"><path d="M0 0h12L6 7z" fill="#333"/></svg></span></div>
  <div class="field f-address">Address <b>*</b></div>
  <span class="btn submit">Submit</span>
</form>

<section class="services abs"></section>
<h2 class="section-title center-title services-title abs">Our <span class="accent">Services</span></h2>
<div class="divider abs" style="top:1215px"><span></span></div>
<p class="services-intro abs">Lorem ipsum dolor sit amet, consectetuer adipiscing elit, sed diam nonummy nibh euismod tincidunt ut laoreet dolore magna aliquam erat volutpat. Ut wisi enim ad minim veniam, quis nostrud exerci tation ullamcorper suscipit lobortis nisl ut aliquip</p>

<svg class="service-ring abs" width="1200" height="2765" viewBox="0 0 1200 2765" aria-hidden="true">
  <path d="M 442 1742 A 210 210 0 1 1 756 1742" fill="none" stroke="#c6c6c6" stroke-width="7"/>
</svg>

<div class="svc-icon abs" style="left:557px;top:1366px"><span class="frame"></span><span class="tile"><svg width="34" height="34" viewBox="0 0 34 34"><path fill="#fff" d="M6 6h22v26H6zM10 10v4h4v-4zm10 0v4h4v-4zM10 18v4h4v-4zm10 0v4h4v-4zm-6 8v6h6v-6z"/></svg></span></div>
<div class="svc-icon abs" style="left:339px;top:1522px"><span class="frame"></span><span class="tile"><svg width="34" height="34" viewBox="0 0 34 34"><rect x="6" y="14" width="18" height="14" fill="#fff"/><rect x="14" y="6" width="14" height="10" fill="#fff" transform="rotate(15 21 11)"/></svg></span></div>
<div class="svc-icon abs" style="left:772px;top:1522px"><span class="frame"></span><span class="tile"><svg width="34" height="34" viewBox="0 0 34 34"><path fill="#fff" d="M8 4h3v28H8zM4 6h26v2H4zM22 18h9v14h-9z"/></svg></span></div>
<div class="svc-icon abs" style="left:401px;top:1701px"><span class="frame"></span><span class="tile"><svg width="34" height="34" viewBox="0 0 34 34"><path fill="#fff" d="M4 22h22v6H4zM8 14h10v8H8zM18 16l8-10 4 2-8 10z"/></svg></span></div>
<div class="svc-icon abs" style="left:712px;top:1701px"><span class="frame"></span><span class="tile"><svg width="34" height="34" viewBox="0 0 34 34"><path fill="#fff" d="M2 20h30v3H2zM8 8h3v20H8zm15 0h3v20h-3zM9 9l8 11h-2L9 12zm16 0l-8 11h2l6-8z"/></svg></span></div>

<div class="core abs" aria-hidden="true"><span class="frame"></span><span class="tile"></span></div>

<div class="svc-label right-al abs" style="left:229px;top:1354px"><h3>Commercial Finance</h3><p>Lorem ipsum dolor sit amet, nsect<br>adipiscing elit, sed diam non wrwer</p></div>
<div class="svc-label right-al abs" style="left:10px;top:1529px"><h3>Business Finance</h3><p>Lorem ipsum dolor sit amet, nsectet<br>adipiscing elit, sed diam non wrwer</p></div>
<div class="svc-label abs" style="left:890px;top:1529px"><h3>Construction Finance</h3><p>Lorem ipsum dolor sit amet, nsectet<br>adipiscing elit, sed diam non wrwer</p></div>
<div class="svc-label right-al abs" style="left:78px;top:1709px"><h3>Equipment Finance</h3><p>Lorem ipsum dolor sit amet, nsectetuer<br>adipiscing elit, sed diam non wrwer</p></div>
<div class="svc-label abs" style="left:816px;top:1709px"><h3>Bridging Finance</h3><p>Lorem ipsum dolor sit amet, nsectetuer<br>adipiscing elit, sed diam non wrwer</p></div>

<h2 class="section-title center-title blog-title abs">Latest <span class="accent">Blog Posts</span></h2>
<div class="divider blog-divider abs"><span></span></div>

<article class="post abs" style="left:79px">
  <div class="post-photo" role="img" aria-label="Photo of a person silhouetted on a rock against a bright blue sky" style="background:linear-gradient(160deg,#8fc4ef,#2e77c4 60%,#17314f)"></div>
  <div class="post-date"><div class="dm">10<br>JAN</div><div class="yr">2017</div></div>
  <h4>LOREM IPSUM DOLOR</h4>
  <p>Sed ut perspiciatis unde omnis iste natus errorluptatem accusa nt ium dolorem que laudantium totam rem aperiam laudantium</p>
  <div class="post-meta"><strong>By :</strong>&nbsp;Sed ut perspiciatis<span class="sep"></span><strong>0</strong>&nbsp;Comments</div>
</article>
<article class="post abs" style="left:435px">
  <div class="post-photo" role="img" aria-label="Photo of a couple meeting with a financial adviser at a table" style="background:linear-gradient(135deg,#e9e6e0,#c9b9a3 50%,#f2efea)"></div>
  <div class="post-date"><div class="dm">10<br>JAN</div><div class="yr">2017</div></div>
  <h4>LOREM IPSUM DOLOR</h4>
  <p>Sed ut perspiciatis unde omnis iste natus errorluptatem accusa nt ium dolorem que laudantium totam rem aperiam laudantium</p>
  <div class="post-meta"><strong>By :</strong>&nbsp;Sed ut perspiciatis<span class="sep"></span><strong>0</strong>&nbsp;Comments</div>
</article>
<article class="post abs" style="left:789px">
  <div class="post-photo" role="img" aria-label="Photo of a calculator and pen on a financial chart" style="background:linear-gradient(135deg,#5a7fa6,#c9d9ea 55%,#7d9cbd)"></div>
  <div class="post-date"><div class="dm">10<br>JAN</div><div class="yr">2017</div></div>
  <h4>LOREM IPSUM DOLOR</h4>
  <p>Sed ut perspiciatis unde omnis iste natus errorluptatem accusa nt ium dolorem que laudantium totam rem aperiam laudantium</p>
  <div class="post-meta"><strong>By :</strong>&nbsp;Sed ut perspiciatis<span class="sep"></span><strong>0</strong>&nbsp;Comments</div>
</article>

<footer class="site-footer abs"></footer>
<h5 class="foot-head abs" style="left:79px">Quick <span class="accent">Links</span></h5>
<h5 class="foot-head abs" style="left:315px">Contact <span class="accent">Details</span></h5>
<h5 class="foot-head abs" style="left:612px">Location <span class="accent">Map</span></h5>
<h5 class="foot-head abs" style="left:990px">Follow <span class="accent">Us</span></h5>

<ul class="foot-links abs">
  <li class="current">HOME</li>
  <li>ABOUT US</li>
  <li>SERVICES</li>
</ul>
<div class="foot-square abs" aria-hidden="true"></div>

<div class="contact abs">
  <div class="name">Marcus Finance</div>
  <p style="margin-top:10px">Sed ut perspiciatis unde omnis iste natus errorluptatem accusa nt ium dolorem 0123456</p>
  <div class="row" style="margin-top:30px"><svg width="14" height="14" viewBox="0 0 24 24"><path fill="#1e9ff2" d="M6.6 10.8a15 15 0 0 0 6.6 6.6l2.2-2.2c.3-.3.7-.4 1-.2 1.1.4 2.3.6 3.6.6.6 0 1 .4 1 1V20c0 .6-.4 1-1 1A17 17 0 0 1 3 4c0-.6.4-1 1-1h3.5c.6 0 1 .4 1 1 0 1.3.2 2.5.6 3.6.1.3 0 .7-.2 1z"/></svg>0198 765 432</div>
  <div class="row" style="margin-top:26px"><svg width="14" height="11" viewBox="0 0 14 11"><rect width="14" height="11" fill="#1e9ff2"/><path d="M0 0l7 6 7-6" fill="none" stroke="#151c26" stroke-width="1.5"/></svg>info@marcusfinance.com</div>
</div>

<div class="map abs" role="img" aria-label="Street map showing the office location"></div>

<ul class="social abs">
  <li><span class="dot"></span>Pagebook</li>
  <li><span class="dot"></span>Chirper</li>
  <li><span class="dot"></span>Worklink</li>
  <li><span class="dot"></span>Searchplus</li>
</ul>

<div class="copyright abs">Copyright © 2017 Marcus Finance. All Rights Reserved</div>

</body>
</html>
```